Vehicle Signage

Please design a graphic layout for a Van signage to advertise the business

"Kestrel Alarm Works"
the logo is in the attached files

Also attached are some icons that represent the fields of service, I would like to use these in the design please
Updates

Reason: I am making some changes to the KAW logo to help match the Vans, I will up load the new files as soon as possible

Target Market(s)

We are targeting people who feel they would like to have some security equipment installed for piece of mind in the the fields of:
"Alarms, Intercoms, CCTV, Access Control"

Industry/Entity Type

Business

Requirements
Must have
• Must be Clear what we do,
it can be icons/pictures or words to represent the service areas of:

```html
<!DOCTYPE html>
<html lang="en">
<head>
<meta charset="utf-8">
<title>Kestrel Alarm Works – Van Rear Signage</title>
<link href="https://fonts.googleapis.com/css2?family=Arimo:wght@700&display=swap" rel="stylesheet">
<style>
  :root {
    --backdrop: #e6e7e9;
    --panel-dark: #000000;
    --panel-glow: #3a3a3c;
    --brand-blue: #1e3cf5;
    --tile-blue: #1aa3e0;
    --ink: #111111;
    --white: #ffffff;
    --alert-red: #d8232a;
  }
  * { margin: 0; padding: 0; box-sizing: border-box; }
  html, body {
    width: 1147px;
    height: 1200px;
    overflow: hidden;
    background: var(--backdrop);
  }
  .signage {
    position: relative;
    width: 1147px;
    height: 1200px;
    font-family: "Arimo", Arial, sans-serif;
  }
  .brand-panel {
    position: absolute;
    left: 123px;
    top: 250px;
    width: 900px;
    height: 420px;
  }
  .brand-panel svg { position: absolute; inset: 0; }
  .brand-mark {
    position: absolute;
    left: 0;
    right: 0;
    top: 38px;
    text-align: center;
    color: var(--brand-blue);
    font-weight: 700;
    font-size: 230px;
    line-height: 1;
    letter-spacing: 14px;
  }
  .brand-name {
    position: absolute;
    left: 0;
    right: 0;
    top: 308px;
    text-align: center;
    color: var(--white);
    font-weight: 700;
    font-size: 44px;
    letter-spacing: 1px;
  }
  .service {
    position: absolute;
    top: 780px;
    width: 240px;
    margin-left: -120px;
    text-align: center;
  }
  .service-tile {
    display: block;
    width: 116px;
    height: 116px;
    margin: 0 auto;
  }
  .service-label {
    display: block;
    margin-top: 10px;
    color: var(--ink);
    font-weight: 700;
    font-size: 28px;
  }
  .service--alarms { left: 179px; }
  .service--intercoms { left: 350px; }
  .service--cctv { left: 718px; }
  .service--access { left: 901px; }
</style>
</head>
<body>
<main class="signage">
  <section class="brand-panel">
    <svg viewBox="0 0 900 420" width="900" height="420" aria-hidden="true">
      <defs>
        <radialGradient id="panelShade" cx="50%" cy="72%" r="60%">
          <stop offset="0" stop-color="var(--panel-glow)"/>
          <stop offset="1" stop-color="var(--panel-dark)"/>
        </radialGradient>
      </defs>
      <path d="M40 0 H860 Q900 0 900 40 V330 Q900 360 870 364 L500 420 H400 L30 364 Q0 360 0 330 V40 Q0 0 40 0 Z"
            fill="url(#panelShade)"/>
    </svg>
    <div class="brand-mark">KAW</div>
    <div class="brand-name">KESTREL ALARM WORKS</div>
  </section>

  <figure class="service service--alarms">
    <svg class="service-tile" viewBox="0 0 116 116" aria-hidden="true">
      <rect x="2" y="2" width="112" height="112" rx="6" fill="var(--tile-blue)" stroke="var(--white)" stroke-width="3"/>
      <circle cx="58" cy="58" r="38" fill="none" stroke="var(--ink)" stroke-width="5"/>
      <path d="M32 50 H46 L72 36 V80 L46 66 H32 Z" fill="var(--ink)"/>
      <path d="M78 48 L86 44 M80 58 H88 M78 68 L86 72" stroke="var(--ink)" stroke-width="4" stroke-linecap="round"/>
    </svg>
    <figcaption class="service-label">Alarms</figcaption>
  </figure>

  <figure class="service service--intercoms">
    <svg class="service-tile" viewBox="0 0 116 116" aria-hidden="true">
      <rect x="2" y="2" width="112" height="112" rx="6" fill="var(--tile-blue)" stroke="var(--white)" stroke-width="3"/>
      <rect x="30" y="16" width="56" height="84" fill="var(--white)" stroke="var(--ink)" stroke-width="3"/>
      <rect x="36" y="22" width="18" height="28" fill="var(--ink)"/>
      <rect x="60" y="22" width="20" height="8" fill="var(--ink)"/>
      <rect x="60" y="34" width="20" height="8" fill="var(--ink)"/>
      <rect x="60" y="46" width="20" height="8" fill="var(--ink)"/>
      <rect x="60" y="58" width="20" height="8" fill="var(--ink)"/>
      <rect x="60" y="70" width="20" height="8" fill="var(--ink)"/>
      <rect x="60" y="82" width="20" height="8" fill="var(--ink)"/>
      <rect x="36" y="58" width="18" height="34" fill="var(--ink)"/>
    </svg>
    <figcaption class="service-label">Intercoms</figcaption>
  </figure>

  <figure class="service service--cctv">
    <svg class="service-tile" viewBox="0 0 116 116" aria-hidden="true">
      <rect x="2" y="2" width="112" height="112" rx="6" fill="var(--tile-blue)" stroke="var(--white)" stroke-width="3"/>
      <rect x="86" y="10" width="10" height="60" fill="var(--ink)"/>
      <rect x="64" y="50" width="26" height="10" fill="var(--ink)"/>
      <path d="M16 62 L70 50 L78 80 L24 92 Z" fill="var(--ink)"/>
      <path d="M18 82 L30 80 L32 90 L20 92 Z" fill="var(--white)"/>
      <circle cx="28" cy="82" r="3" fill="var(--alert-red)"/>
    </svg>
    <figcaption class="service-label">CCTV</figcaption>
  </figure>

  <figure class="service service--access">
    <svg class="service-tile" viewBox="0 0 116 116" role="img" aria-label="Fingerprint scan icon">
      <rect x="2" y="2" width="112" height="112" rx="6" fill="var(--tile-blue)" stroke="var(--white)" stroke-width="3"/>
      <ellipse cx="58" cy="60" rx="30" ry="38" fill="#1b5a8c"/>
      <rect x="10" y="44" width="96" height="5" fill="var(--alert-red)"/>
    </svg>
    <figcaption class="service-label">Access Conl.</figcaption>
  </figure>
</main>
</body>
</html>
```